research new packaging for fresh rolls, plastic bag, no limit?

Family business: Manufacture and sale of different types of fresh bread since 1992 specializes in pita bread. This is a HANDMADE bread production company and FRESH delivered that morning. The plan is to release a new range of breads including: pita bread burger, hot dog bread, bagel, ... Our company wants a new model bag of bread, unfolded different type of bread FRESH in different colors. You have all seen radius sandwich bread in large area? I want better. I take the box of my father, made me prove that the future is already in place;) We look forward to you! Do not hesitate to contact us for more information. The joint "some ideas" and our logo.

Target Market(s)

We deliver grocers, and restaurants (food made or bistro). For grocers, target customers are young people, housewives, families.

Industry/Entity Type

Bakery

Font styles to use
Serif
Sans Serif
Decorative
Script

Requirements
Must have
• - Attached is our LOGO (.png) - Our brand must be easily identifiable. - That every kind of bread are recognizable by its color. (Example: red for sandwich bread, blue for pita bread ...). But the model of each bag is more or less the same. - (What are the age of the family business since 1992) - Bread FRESH, made in France, - Weight: 500g - Recipe idea - Nutrition facts - Contact: Website, Facebook, email, telephone, address = ° www. lmtbakery.example ° Lantern ° °contact@lmtbakery.example the fresh pita 0162839405 14 Rue des Tilleuls 93100 Montreuil printed bag all the way around, so spread the information. The bag should be about 40cm tall, 25 wide, the bellows would be 12cm "thickness". I foresee a bellows at the bottom of the bag for the package to stand up, and a bagger that will allow us to close the package with a ring where the date will be displayed.
Nice to have
• Same color for all our breads package. And a small color-coded to differentiate our kind of breads (eg www.corvinbakeries.example where the bag is almost the same and the difference is a small colorful acronym) No added coloring or flavoring Information to have on the bag A sandwich filled photo? Red? Like all bread existing brands? Our company is called "Lune-de-miel" we can find a connection? (Or not) (not mandatory)
Should not have
• To you tell me :)

```html
<!DOCTYPE html>
<html lang="fr">
<head>
<meta charset="utf-8">
<title>Lune-de-miel Bakery – Pain Burger</title>
<link rel="stylesheet" href="https://fonts.googleapis.com/css2?family=Oswald:wght@400;600&family=Roboto+Condensed:wght@400&display=swap">
<style>
  :root {
    --backdrop: #fbfbfb;
    --kraft: #f2dbae;
    --kraft-shade: #e6cc9a;
    --bakery-green: #077a4f;
    --ribbon-dark: #05603e;
    --bun-orange: #ee7a2c;
    --bun-gold: #f6a94a;
    --bun-red: #d9532a;
    --ink-brown: #6b4a22;
    --ink-soft: #8a6a42;
  }
  * { margin: 0; padding: 0; box-sizing: border-box; }
  html, body {
    width: 1200px; height: 720px; overflow: hidden;
    background: var(--backdrop);
  }
  .canvas {
    position: relative; width: 1200px; height: 720px;
  }
  .bag-front {
    position: absolute; left: 390px; top: 40px;
    width: 420px; height: 640px;
    background: var(--kraft);
    overflow: hidden;
  }
  .bag-front__fold {
    position: absolute; left: 0; top: 0; width: 100%; height: 14px;
    background: var(--kraft-shade);
  }
  .bag-front__bands {
    position: absolute; inset: 0;
  }
  .range-ribbon {
    position: absolute; left: 50%; top: 78px;
    transform: translateX(-50%);
    width: 260px; height: 70px;
  }
  .range-ribbon__label {
    position: absolute; left: 30px; right: 30px; top: 8px; height: 44px;
    display: flex; align-items: center; justify-content: center;
    font-family: "Oswald", sans-serif; font-weight: 600;
    font-size: 21px; letter-spacing: 2px; color: #fff;
  }
  .hero-photo {
    position: absolute; left: 60px; top: 170px;
    width: 310px; height: 250px; border-radius: 50%;
    background: radial-gradient(ellipse at 40% 35%, var(--bun-gold) 0%, var(--bun-orange) 55%, var(--bun-red) 100%);
  }
  .brand-name {
    position: absolute; left: 60px; top: 250px; width: 310px;
    text-align: center;
    font-family: "Oswald", sans-serif; font-weight: 400;
    font-size: 40px; line-height: 1.1; color: var(--ink-brown);
    text-transform: uppercase;
  }
  .product-facts {
    position: absolute; left: 120px; top: 540px; width: 200px;
    text-align: center;
    font-family: "Roboto Condensed", sans-serif;
    font-size: 8px; line-height: 1.6; color: var(--ink-soft);
    text-transform: uppercase;
  }
  .product-facts__weight { text-transform: none; }
</style>
</head>
<body>
<main class="canvas">
  <section class="bag-front">
    <svg class="bag-front__bands" viewBox="0 0 420 640" width="420" height="640" aria-hidden="true">
      <polygon points="0,330 240,640 0,640" fill="var(--bakery-green)"/>
      <polygon points="420,380 420,640 240,640" fill="var(--bakery-green)"/>
    </svg>
    <div class="bag-front__fold"></div>

    <div class="range-ribbon">
      <svg viewBox="0 0 260 70" width="260" height="70" aria-hidden="true">
        <polygon points="0,22 36,18 36,58 10,62 20,42" fill="var(--bakery-green)"/>
        <polygon points="260,14 224,18 224,56 250,52 240,34" fill="var(--bakery-green)"/>
        <polygon points="30,52 38,58 38,50" fill="var(--ribbon-dark)"/>
        <polygon points="230,50 222,56 222,48" fill="var(--ribbon-dark)"/>
        <rect x="30" y="8" width="200" height="44" rx="5" fill="var(--bakery-green)"/>
        <rect x="35" y="13" width="190" height="34" rx="4" fill="none" stroke="#fff" stroke-width="1.5"/>
      </svg>
      <span class="range-ribbon__label">PAIN BURGER</span>
    </div>

    <div class="hero-photo" role="img" aria-label="Photo de pains burger aux graines de sésame"></div>
    <p class="brand-name">Lune-de-miel<br>Bakery</p>

    <p class="product-facts">
      Sans colorant ou arôme ajouté<br>
      - Fabriqué en France -<br>
      <span class="product-facts__weight">500g</span>
    </p>
  </section>
</main>
</body>
</html>
```